IT Company Business Card Rebranding

We want to modernize our business cards massively. We want to incorporate aspects of our old business card such as the white and geometric design with the blues of another icon. Existing Logo, old business card and icon are all attached.

We are a modern IT company that provides support for new and growing technologies and want our business cards to be modern yet professional.
Updates

Industry/Entity Type

Information Technology

Contact Information for Business Card

Roughly 43 : 26 or 1075 x 650 px

Font styles to use
Serif

Colors
0492cd
3276b5
33a6d7
86cfc6
cfeae6
cee9f5
ffffff

Requirements
Must have
• Modern yet professional
Nice to have
• We would like to incorporate the blues of our existing logo and of the icon provided. Really like the design of the icon.
Should not have
• Too Decorative. Just simple and professional.
• Not have the circle icon, as it is a copyrighted icon, I just like the colors and the geometric design

```html
<!DOCTYPE html>
<html lang="en">
<head>
<meta charset="utf-8">
<title>Nexa Systems — Business Card</title>
<link rel="stylesheet" href="https://fonts.googleapis.com/css2?family=PT+Serif:wght@400;700&display=swap">
<style>
  :root {
    --page-bg: #eef1f4;
    --card-white: #ffffff;
    --brand-blue: #0492cd;
    --deep-blue: #3276b5;
    --sky-blue: #33a6d7;
    --mint: #86cfc6;
    --pale-mint: #cfeae6;
    --pale-sky: #cee9f5;
    --text-grey: #8a8d91;
    --name-grey: #9a9da1;
  }
  html, body {
    margin: 0;
    width: 1200px;
    height: 1022px;
    overflow: hidden;
    background: var(--page-bg);
    font-family: "PT Serif", Georgia, serif;
  }
  .card {
    position: absolute;
    left: 62px;
    top: 186px;
    width: 1075px;
    height: 650px;
    background: var(--card-white);
    border-radius: 26px;
    overflow: hidden;
    box-shadow: 0 10px 30px rgba(40, 60, 80, 0.14);
  }
  .facets {
    position: absolute;
    left: 0;
    top: 0;
    width: 1075px;
    height: 650px;
  }
  .brand {
    position: absolute;
    left: 120px;
    top: 110px;
    width: 300px;
    text-align: center;
  }
  .brand-dot {
    width: 120px;
    height: 120px;
    border-radius: 50%;
    background: var(--brand-blue);
    margin: 0 auto 34px;
  }
  .brand-name {
    font-size: 38px;
    letter-spacing: 8px;
    color: var(--name-grey);
    font-weight: 400;
    white-space: nowrap;
  }
  .divider {
    position: absolute;
    left: 440px;
    top: 400px;
    width: 575px;
    height: 2px;
    background: var(--deep-blue);
  }
  .contact {
    position: absolute;
    right: 60px;
    top: 262px;
    text-align: right;
    font-size: 22px;
    line-height: 38px;
    color: var(--text-grey);
  }
  .contact-row {
    display: flex;
    justify-content: flex-end;
    align-items: center;
    gap: 14px;
  }
  .contact-row svg { width: 18px; height: 18px; }
  .person {
    position: absolute;
    left: 440px;
    top: 418px;
    color: var(--text-grey);
  }
  .person-name {
    font-size: 44px;
    font-weight: 700;
    color: var(--deep-blue);
    letter-spacing: 2px;
    margin: 0;
    line-height: 1.1;
  }
  .person-role {
    font-size: 22px;
    letter-spacing: 3px;
    margin: 4px 0 10px;
    padding-top: 6px;
    border-top: 1px solid #c9ccd0;
    display: inline-block;
  }
  .person-note {
    font-size: 24px;
    line-height: 34px;
    letter-spacing: 1px;
  }
</style>
</head>
<body>
  <div class="card">
    <svg class="facets" viewBox="0 0 1075 650" role="img" aria-label="Faint geometric facets in pale blue and mint">
      <defs>
        <linearGradient id="facetTone" x1="0" y1="0" x2="1" y2="1">
          <stop offset="0" stop-color="#cee9f5" stop-opacity="0.7"/>
          <stop offset="1" stop-color="#cfeae6" stop-opacity="0.5"/>
        </linearGradient>
      </defs>
      <polygon points="700,0 1075,0 1075,420 900,380 760,250" fill="url(#facetTone)"/>
    </svg>

    <div class="brand">
      <div class="brand-dot"></div>
      <div class="brand-name">NEXA SYSTEMS</div>
    </div>

    <div class="contact">
      <div class="contact-row">+ 330 5550 1142
        <svg viewBox="0 0 24 24"><path d="M6 3l3 0 2 5-2 1.5a11 11 0 0 0 5.5 5.5L16 13l5 2v3a2 2 0 0 1-2 2A16 16 0 0 1 4 5a2 2 0 0 1 2-2z" fill="none" stroke="#3276b5" stroke-width="2"/></svg>
      </div>
      <div class="contact-row">info@northgridtech.com
        <svg viewBox="0 0 24 24"><rect x="3" y="5" width="18" height="14" rx="1" fill="none" stroke="#3276b5" stroke-width="2"/><path d="M3 6l9 7 9-7" fill="none" stroke="#3276b5" stroke-width="2"/></svg>
      </div>
      <div class="contact-row">www.northgridtech.com
        <svg viewBox="0 0 24 24"><circle cx="12" cy="12" r="9" fill="none" stroke="#3276b5" stroke-width="2"/><path d="M3 12h18M12 3c3 3 3 15 0 18M12 3c-3 3-3 15 0 18" fill="none" stroke="#3276b5" stroke-width="1.6"/></svg>
      </div>
    </div>

    <div class="divider"></div>

    <div class="person">
      <h1 class="person-name">JONAH</h1>
      <div class="person-role">TECHNICAL SERVICES</div>
      <div class="person-note">Roughly 43 :<br>26 or 1075 x 650 px</div>
    </div>
  </div>
</body>
</html>
```